Flyer for the Lumen 2025 Conference

I am looking to produce a flyer for our upcoming conference, Lumen 2025. This is an annual conference that we plan to publicize on social media. The ideal designer will create a flyer that is eye-catching and effectively communicates the key information. Please see attached our logo, speaker photo, and flyer content.

Target Market(s)

All demographics

Industry/Entity Type

Christian

Font styles to use
Sans Serif

Requirements
Should not have
• Cross, church

```html
<!DOCTYPE html>
<html lang="en">
<head>
<meta charset="utf-8">
<title>Lumen 2025 Conference Flyers</title>
<link rel="stylesheet" href="https://fonts.googleapis.com/css2?family=Oswald:wght@300;400;500;600;700&family=Montserrat:wght@800&display=swap">
<style>
:root{
  --stage:#8a8a8a;
  --orange:#f7941d;
  --orange-deep:#ff6a00;
  --navy:#0f3a66;
  --white:#ffffff;
  --ink:#1a1a1a;
}
*{margin:0;padding:0;box-sizing:border-box}
html,body{width:1200px;height:406px;overflow:hidden;background:var(--stage)}
body{position:relative;font-family:"Oswald",sans-serif}
.flyer{position:absolute;top:18px;width:369px;height:369px;display:flex;overflow:hidden}
.flyer--storm{left:28px;
  --left-bg:linear-gradient(180deg,#2a4a78 0%,#1b355e 45%,#0a1830 100%);
  --right-bg:var(--navy);--head:var(--white);--label:var(--orange);--body:var(--white);
  --more:var(--white);--icon:var(--white);--topic:var(--orange);
  --rule:var(--orange);--title:var(--white);--name-bg:var(--white);--name-fg:var(--navy);
  --photo:linear-gradient(180deg,#14406e 0%,#1d5ba8 50%,#0d2c52 100%)}
.flyer--ember{left:412px;
  --left-bg:linear-gradient(180deg,#ff6a00 0%,#fb6400 60%,#d84000 100%);
  --right-bg:#000;--head:var(--ink);--label:var(--ink);--body:var(--ink);
  --more:var(--white);--icon:var(--white);--topic:var(--white);
  --rule:var(--ink);--title:var(--white);--name-bg:var(--orange-deep);--name-fg:var(--white);
  --photo:linear-gradient(180deg,#050505 0%,#1d4f9c 50%,#070707 100%)}
.flyer--light{left:803px;
  --left-bg:linear-gradient(180deg,#ffffff 0%,#ffffff 55%,#e2e2e2 100%);
  --right-bg:var(--navy);--head:var(--navy);--label:var(--navy);--body:var(--navy);
  --more:var(--navy);--icon:var(--orange-deep);--topic:var(--orange-deep);
  --rule:var(--navy);--title:var(--orange-deep);--name-bg:var(--orange-deep);--name-fg:var(--white);
  --photo:linear-gradient(180deg,#14406e 0%,#1d5ba8 50%,#0d2c52 100%)}

.info{position:relative;width:220px;height:100%;background:var(--left-bg);color:var(--body)}
.info > *{position:absolute;left:22px}
.kicker{top:18px;font-size:19px;font-weight:300;color:var(--head);white-space:nowrap}
.topic{top:57px;font-family:"Montserrat",sans-serif;font-weight:800;font-size:15px;letter-spacing:1.5px;color:var(--topic)}
.title{font-weight:700;font-size:58px;line-height:1;color:var(--title);letter-spacing:.5px}
.title--name{top:70px}
.title--year{top:126px}
.rule{height:1px;width:181px;background:var(--rule)}
.rule--top{top:192px}.rule--bottom{top:226px}
.schedule{top:195px;width:181px;height:29px;display:flex;text-align:center}
.schedule .cell{flex:1;display:flex;flex-direction:column;justify-content:center;gap:1px}
.schedule .cell + .cell{border-left:1.5px solid var(--body)}
.label{font-size:10px;color:var(--label);font-weight:400;line-height:1.15}
.value{font-size:9.5px;font-weight:400;line-height:1.15;white-space:nowrap}
.venue{top:233px;width:196px;left:12px;text-align:center;line-height:1.2}
.venue .label{display:block;margin-bottom:1px}
.venue p{font-size:9.5px;font-weight:400;white-space:nowrap}
.more{top:279px;font-size:8px;font-weight:700;letter-spacing:2.5px;color:var(--more)}
.download{top:289px;font-size:6.3px;font-weight:500;white-space:nowrap;color:var(--more)}
.stores{top:298px;display:flex;gap:4px}
.store{width:50px;height:13px;background:#000;border:.6px solid #bbb;border-radius:2px}
.contact{top:318px;list-style:none;font-size:6px;font-weight:600;line-height:10px;color:var(--more)}
.contact li{display:flex;align-items:center;gap:3px}
.contact svg{width:6px;height:6px;color:var(--icon)}
.live{top:352px;left:23px;width:46px;height:12px;border-radius:6px;background:linear-gradient(90deg,#3b3fb8,#5a6fe0);display:flex;align-items:center;justify-content:center;gap:4px;color:var(--white);font-size:4.5px;font-weight:600;line-height:1;text-align:center}
.live i{display:block;width:7px;height:5px;background:#e53935;border-radius:1px}

.speaker-panel{position:relative;width:149px;height:100%;background:var(--right-bg);color:var(--white)}
.brand{position:absolute;top:30px;left:0;width:100%;text-align:center}
.brand-name{display:inline-flex;align-items:center;gap:4px;font-size:24px;font-weight:400;line-height:1;color:var(--white);letter-spacing:.5px}
.brand-name i{display:block;width:7px;height:7px;border-radius:50%;background:var(--orange)}
.portrait{position:absolute;top:96px;left:5px;width:139px;height:232px;background:var(--photo);border-radius:40px 40px 6px 6px;opacity:.9}
.speaker-label{position:absolute;top:331px;left:0;width:100%;text-align:center;font-size:7px;letter-spacing:4.5px;font-weight:500}
.speaker-name{position:absolute;top:340px;left:18px;width:113px;height:13px;background:var(--name-bg);color:var(--name-fg);font-size:11px;font-weight:400;line-height:13px;text-align:center;white-space:nowrap}
</style>
</head>
<body>

<article class="flyer flyer--storm">
  <section class="info">
    <p class="kicker">A Prophetic Conference</p>
    <p class="topic">TOPIC</p>
    <h1 class="title title--name">LUMEN</h1>
    <p class="title title--year">2025</p>
    <div class="rule rule--top"></div>
    <div class="schedule">
      <div class="cell"><span class="label">DATE</span><span class="value">Friday December 26th</span></div>
      <div class="cell"><span class="label">TIME</span><span class="value">6:30PM - 9:00PM</span></div>
    </div>
    <div class="rule rule--bottom"></div>
    <div class="venue"><span class="label">LOCATION</span><p>The Harborview Performing Arts Center</p><p>88 Linden Avenue Millbrook, Maine 04010</p></div>
    <p class="more">MORE INFO</p>
    <p class="download">Download the OREVANTH App to stay updated on the event</p>
    <div class="stores"><span class="store"></span><span class="store"></span></div>
    <ul class="contact">
      <li><svg viewBox="0 0 10 10"><path d="M2 1l2 2-1 1.2c.6 1.3 1.5 2.2 2.8 2.8L7 6l2 2-1.3 1.3C4.5 9 1 5.5.7 2.3z" fill="currentColor"/></svg>207 555 0142</li>
      <li><svg viewBox="0 0 10 10"><rect x="1" y="2" width="8" height="6" fill="none" stroke="currentColor"/><path d="M1 2l4 3 4-3" fill="none" stroke="currentColor"/></svg>contact@orevanth.org</li>
      <li><svg viewBox="0 0 10 10"><circle cx="5" cy="5" r="4" fill="none" stroke="currentColor"/><path d="M1 5h8M5 1c-2 2.5-2 5.5 0 8M5 1c2 2.5 2 5.5 0 8" fill="none" stroke="currentColor" stroke-width=".8"/></svg>www.orevanth.org</li>
    </ul>
    <div class="live"><span>LIVE<br>STREAMING</span><i></i></div>
  </section>
  <section class="speaker-panel">
    <div class="brand"><span class="brand-name"><i></i>OREVANTH</span></div>
    <div class="portrait" role="img" aria-label="Photo of the speaker seated in a blue suit"></div>
    <p class="speaker-label">SPEAKER</p>
    <p class="speaker-name">PROPHET ELIAS MARSH</p>
  </section>
</article>

<article class="flyer flyer--ember">
  <section class="info">
    <p class="kicker">A Prophetic Conference</p>
    <p class="topic">TOPIC</p>
    <h1 class="title title--name">LUMEN</h1>
    <p class="title title--year">2025</p>
    <div class="rule rule--top"></div>
    <div class="schedule">
      <div class="cell"><span class="label">DATE</span><span class="value">Saturday December 27th</span></div>
      <div class="cell"><span class="label">TIME</span><span class="value">5:30PM - 8:00PM</span></div>
    </div>
    <div class="rule rule--bottom"></div>
    <div class="venue"><span class="label">LOCATION</span><p>The Harborview Performing Arts Center</p><p>88 Linden Avenue Millbrook, Maine 04010</p></div>
    <p class="more">MORE INFO</p>
    <p class="download">Download the OREVANTH App to stay updated on the event</p>
    <div class="stores"><span class="store"></span><span class="store"></span></div>
    <ul class="contact">
      <li><svg viewBox="0 0 10 10"><path d="M2 1l2 2-1 1.2c.6 1.3 1.5 2.2 2.8 2.8L7 6l2 2-1.3 1.3C4.5 9 1 5.5.7 2.3z" fill="currentColor"/></svg>207 555 0142</li>
      <li><svg viewBox="0 0 10 10"><rect x="1" y="2" width="8" height="6" fill="none" stroke="currentColor"/><path d="M1 2l4 3 4-3" fill="none" stroke="currentColor"/></svg>contact@orevanth.org</li>
      <li><svg viewBox="0 0 10 10"><circle cx="5" cy="5" r="4" fill="none" stroke="currentColor"/><path d="M1 5h8M5 1c-2 2.5-2 5.5 0 8M5 1c2 2.5 2 5.5 0 8" fill="none" stroke="currentColor" stroke-width=".8"/></svg>www.orevanth.org</li>
    </ul>
    <div class="live"><span>LIVE<br>STREAMING</span><i></i></div>
  </section>
  <section class="speaker-panel">
    <div class="brand"><span class="brand-name"><i></i>OREVANTH</span></div>
    <div class="portrait" role="img" aria-label="Photo of the speaker seated in a blue suit"></div>
    <p class="speaker-label">SPEAKER</p>
    <p class="speaker-name">PROPHET ELIAS MARSH</p>
  </section>
</article>

<article class="flyer flyer--light">
  <section class="info">
    <p class="kicker">A Prophetic Conference</p>
    <p class="topic">TOPIC</p>
    <h1 class="title title--name">LUMEN</h1>
    <p class="title title--year">2025</p>
    <div class="rule rule--top"></div>
    <div class="schedule">
      <div class="cell"><span class="label">DATE</span><span class="value">Sunday December 26th</span></div>
      <div class="cell"><span class="label">TIME</span><span class="value">4:30PM - 7:00PM</span></div>
    </div>
    <div class="rule rule--bottom"></div>
    <div class="venue"><span class="label">LOCATION</span><p>The Harborview Performing Arts Center</p><p>88 Linden Avenue Millbrook, Maine 04010</p></div>
    <p class="more">MORE INFO</p>
    <p class="download">Download the OREVANTH App to stay updated on the event</p>
    <div class="stores"><span class="store"></span><span class="store"></span></div>
    <ul class="contact">
      <li><svg viewBox="0 0 10 10"><path d="M2 1l2 2-1 1.2c.6 1.3 1.5 2.2 2.8 2.8L7 6l2 2-1.3 1.3C4.5 9 1 5.5.7 2.3z" fill="currentColor"/></svg>207 555 0142</li>
      <li><svg viewBox="0 0 10 10"><rect x="1" y="2" width="8" height="6" fill="none" stroke="currentColor"/><path d="M1 2l4 3 4-3" fill="none" stroke="currentColor"/></svg>contact@orevanth.org</li>
      <li><svg viewBox="0 0 10 10"><circle cx="5" cy="5" r="4" fill="none" stroke="currentColor"/><path d="M1 5h8M5 1c-2 2.5-2 5.5 0 8M5 1c2 2.5 2 5.5 0 8" fill="none" stroke="currentColor" stroke-width=".8"/></svg>www.orevanth.org</li>
    </ul>
    <div class="live"><span>LIVE<br>STREAMING</span><i></i></div>
  </section>
  <section class="speaker-panel">
    <div class="brand"><span class="brand-name"><i></i>OREVANTH</span></div>
    <div class="portrait" role="img" aria-label="Photo of the speaker seated in a blue suit"></div>
    <p class="speaker-label">SPEAKER</p>
    <p class="speaker-name">PROPHET ELIAS MARSH</p>
  </section>
</article>

</body>
</html>
```